Business Card Design For DJ Company

I'm rebranding my wedding and event dj company. I am looking for a modern, luxury, & fun design to match my new logo and website design. Please see attached logo and new webpage design. Colors should match. Design should flow with logo and website for recognition. I want to attract young adults. I plan on printing metallic finish cards so please keep hat in mind.

Target Market(s)

Millennials

Contact Information for Business Card

Name: Dario Colvento
Company: Cedar Hollow Mix DJ
Services: DJ – Photo Booth – Event Lighting – LED Robot

Website: www.cedarhollowmixdj.example
Email: dario@cedarhollowmixdj.example
Phone: (555)417-9382

Instagram: @chmixdj
Facebook: @chmixdj
Twitter - @chmixdj

Se Habla Español

Font styles to use
Serif
Sans Serif

Colors

Designer to choose colors to be used in the design.

Requirements
Nice to have
• Transparent Gradient background - Image related to weddings

```html
<!DOCTYPE html>
<html lang="en">
<head>
<meta charset="utf-8">
<title>Cedar Hollow Mix DJ – Business Card</title>
<link rel="stylesheet" href="https://fonts.googleapis.com/css2?family=Lato:wght@400;700;900&family=Baloo+2:wght@600&display=swap">
<style>
  :root {
    --orange: #f7941d;
    --blue: #27a8e0;
    --green: #8cc63f;
    --black: #050505;
    --white: #ffffff;
    --stage: #e9e6e1;
    --band: #fde3c4;
  }
  * { margin: 0; padding: 0; box-sizing: border-box; }
  html, body { width: 1200px; height: 1012px; overflow: hidden; }
  body { background: var(--stage); position: relative; font-family: "Lato", sans-serif; }

  .card { position: absolute; width: 744px; height: 423px; border-radius: 22px; overflow: hidden; }
  .card svg.art { position: absolute; inset: 0; }

  /* Front (contact) side */
  .card--front { left: 392px; top: 63px; background: var(--black); }
  .holder { position: absolute; right: 30px; top: 28px; text-align: right; color: var(--white); }
  .holder__name { font-weight: 900; font-size: 25px; letter-spacing: .3px; }
  .holder__title { font-weight: 900; font-size: 21px; margin-top: 4px; }

  .brand { position: absolute; display: flex; align-items: center; gap: 12px; }
  .brand__dot { width: 26px; height: 26px; border-radius: 50%; background: var(--blue); flex: none; }
  .brand__name { font-weight: 900; color: var(--orange); line-height: 1.05; text-transform: uppercase; }
  .card--front .brand { left: 52px; top: 170px; }
  .card--front .brand__name { font-size: 30px; }

  .social { position: absolute; left: 98px; top: 362px; display: flex; gap: 17px; }
  .social__ring { width: 32px; height: 32px; border-radius: 50%; border: 2px solid var(--orange); }

  .contact { position: absolute; right: 30px; top: 313px; list-style: none; color: var(--white); font-size: 17px; text-align: right; }
  .contact li { height: 33px; display: flex; justify-content: flex-end; align-items: center; gap: 6px; }
  .contact svg { width: 16px; height: 16px; }

  /* Back (services) side */
  .card--back { left: 50px; top: 536px; background: var(--white); }
  .wave-band { position: absolute; left: 0; right: 0; top: 45px; height: 96px;
    background: linear-gradient(90deg, rgba(253,227,196,.3), var(--band) 20%, var(--band) 80%, rgba(253,227,196,.3)); }
  .card--back .brand { left: 50%; top: 70px; transform: translateX(-50%); }
  .card--back .brand__name { font-size: 32px; white-space: nowrap; }

  .service-photo { position: absolute; width: 124px; height: 124px; border-radius: 50%; border: 4px solid var(--blue); }
  .service-label { position: absolute; font-family: "Baloo 2", sans-serif; font-weight: 600; font-size: 21px; color: var(--orange); transform: translate(-50%, -50%); white-space: nowrap; }
  .photo--dj { left: 61px; top: 195px; background: radial-gradient(circle at 50% 40%, #9a4fd8, #3a1a6e 60%, #150a2e); }
  .photo--booth { left: 228px; top: 277px; background: radial-gradient(circle at 50% 45%, #d9d3d6, #8b8088 70%, #5b5260); }
  .photo--lighting { left: 395px; top: 195px; background: radial-gradient(circle at 45% 40%, #6d7bd8, #2a1f6a 60%, #0b0b24); }
  .photo--robot { left: 562px; top: 277px; background: radial-gradient(circle at 50% 50%, #3f8dff, #0f3fb0 60%, #061a52); }
</style>
</head>
<body>

<section class="card card--front" aria-label="Business card front">
  <svg class="art" width="744" height="423" viewBox="0 0 744 423" aria-hidden="true">
    <rect width="744" height="423" fill="var(--orange)"/>
    <path d="M0,80 Q330,5 744,185 L744,423 L0,423 Z" fill="var(--blue)"/>
    <path d="M0,95 Q320,28 744,215 L744,423 L0,423 Z" fill="var(--black)"/>
    <path d="M0,100 Q160,55 378,76 Q160,68 0,118 Z" fill="var(--green)"/>
  </svg>

  <div class="holder">
    <div class="holder__name">DARIO COLVENTO</div>
    <div class="holder__title">TITLE</div>
  </div>

  <div class="brand">
    <span class="brand__dot"></span>
    <span class="brand__name">Cedar Hollow<br>Mix DJ</span>
  </div>

  <div class="social" aria-label="Social media @chmixdj">
    <span class="social__ring"></span>
    <span class="social__ring"></span>
    <span class="social__ring"></span>
  </div>

  <ul class="contact">
    <li>
      <svg viewBox="0 0 16 16" aria-hidden="true"><circle cx="8" cy="8" r="8" fill="var(--orange)"/><path d="M5 4.5l1.6-.4.9 2-1 .8a5 5 0 0 0 2.6 2.6l.8-1 2 .9-.4 1.6c-3.6.3-6.8-2.9-6.5-6.5z" fill="var(--black)"/></svg>
      (555)417-9382
    </li>
    <li>
      <svg viewBox="0 0 16 16" aria-hidden="true"><circle cx="8" cy="8" r="8" fill="var(--orange)"/><rect x="4" y="5.5" width="8" height="5.5" fill="none" stroke="var(--black)" stroke-width="1.2"/><path d="M4 5.5l4 3 4-3" fill="none" stroke="var(--black)" stroke-width="1.2"/></svg>
      dario@cedarhollowmixdj.example
    </li>
    <li>
      <svg viewBox="0 0 16 16" aria-hidden="true"><circle cx="8" cy="8" r="7" fill="none" stroke="var(--orange)" stroke-width="1.6"/><ellipse cx="8" cy="8" rx="3" ry="7" fill="none" stroke="var(--orange)" stroke-width="1.2"/><path d="M1 8h14M2.5 4.5h11M2.5 11.5h11" stroke="var(--orange)" stroke-width="1.1"/></svg>
      www.cedarhollowmixdj.example
    </li>
  </ul>
</section>

<section class="card card--back" aria-label="Business card back">
  <div class="wave-band" role="img" aria-label="Faint sound wave band"></div>

  <div class="brand">
    <span class="brand__dot"></span>
    <span class="brand__name">Cedar Hollow Mix DJ</span>
  </div>

  <svg class="art" width="744" height="423" viewBox="0 0 744 423" aria-hidden="true">
    <path d="M123,257 L290,339 L457,257 L624,339" fill="none" stroke="var(--blue)" stroke-width="3"/>
  </svg>

  <div class="service-photo photo--dj" role="img" aria-label="DJ performing at a party with purple lights"></div>
  <div class="service-photo photo--booth" role="img" aria-label="Guests posing with photo booth props"></div>
  <div class="service-photo photo--lighting" role="img" aria-label="Stage beams of event lighting"></div>
  <div class="service-photo photo--robot" role="img" aria-label="LED robot performer glowing blue"></div>

  <span class="service-label" style="left:290px; top:186px;">Photo Booth</span>
  <span class="service-label" style="left:630px; top:186px;">LED Robot</span>
  <span class="service-label" style="left:120px; top:352px;">DJ</span>
  <span class="service-label" style="left:457px; top:352px;">Event Lighting</span>
</section>

</body>
</html>
```